Nutrigenomics Business card design

Nutrigenomics is an exciting emerging field where I sequence the DNA from a saliva swab and then tailor a personalised nutritional program according to the persons genetics. It is possible to turn down undesirable genes that may be stuck "on" all the time causing inflammation etc. Equally important we switch "on" genes that might be stuck "off" as is often the case with autism. A large portion of my clients are autistic children. We see huge changes in functionality with the appropriate changes in diet to regulate their gene expression. This technology is definitely the way of the future.
I need a logo that will clearly show the combination of genetics with nutrition. The word "Nutrigenomics" still isn't in common use yet. I'm thinking maybe a DNA helix - (I think most people associate a helix with DNA or genes, but I'm open to suggestions) Combined somehow with food - preferably vegetables/ fruit/ meat/eggs etc. Definitely not grains or dairy - we take autistic kids off those 2 food groups straight away.
Green in it somewhere? I somehow associates healthy living / whole foods nutrition with the colour green. You guys know more about colours than me :-)
Maybe a helix could morph into a body shape filled with foods (along the lines of "you are what you eat" or something...)

Target Market(s)

The majority of my clients to date are people in their 40's wanting to improve their health or their children's health.

Industry/Entity Type

Nutrition

Contact Information for Business Card

Front of card:
Dr Moira Crandle (B App Sci, PhD Molecular Pathology)
Certified Vitalorin Practitioner and LUMO Nutritionist
247 Pellbrook Rd, Pellbrook
0417836254
dr.moiracrandle@examplemail.com.au
drmoiracrandle.com.au
Back of card:
Small Photo of me, Dr Moira Crandle
Specialises in Autism, ADHD, Fussy Eaters, Gut Issues, Food Intolerances, Healthy Ageing

Logo Text

Dr Moira Crandle

Logo styles of interest
Pictorial/Combination Logo
Character Logo
Requirements
Must have
• A logo showing a clear link between genes and nutrition
The box for what I want written on the card is not coming up when I try to edit so I'll put it here....
Front of card:
Dr Moira Crandle
(B App Sci, PhD Molecular Pathology) in smaller writing under my name

Certified Nutrigenomist
Certified LUMO Nutritionist

then use your nice symbols for the address, ph etc as below

247 Pellbrook Rd, Pellbrook
0417836254
dr.moiracrandle@examplemail.com.au
www.drmoiracrandle.com.au

Back of card:
Small Photo of me
Dr Moira Crandle
Specialises in:
Nutrigenomics
Healthy Ageing
Autism / ADHD
Gut Issues
Food Intolerances
Should not have
• No bread or grains of any sort
No dairy - milk cheese etc

```html
<!DOCTYPE html>
<html lang="en">
<head>
<meta charset="utf-8">
<title>Dr Moira Crandle – Business Card Back</title>
<link rel="stylesheet" href="https://fonts.googleapis.com/css2?family=Tinos:wght@400&display=swap">
<style>
  :root {
    --brand-green: #3a9c45;
    --paper: #ffffff;
    --ink: #111111;
    --portrait-light: #c9774a;
    --portrait-dark: #3a1f16;
  }
  * { margin: 0; padding: 0; box-sizing: border-box; }
  html, body {
    width: 1200px;
    height: 693px;
    overflow: hidden;
    background: var(--paper);
  }
  .card {
    position: relative;
    width: 1200px;
    height: 693px;
    background: var(--paper);
    font-family: "Tinos", "Times New Roman", serif;
    color: var(--ink);
  }
  .side-band {
    position: absolute;
    left: 1028px;
    top: 47px;
    width: 149px;
    height: 614px;
    background: var(--brand-green);
  }
  .portrait {
    position: absolute;
    left: 461px;
    top: 82px;
    width: 142px;
    height: 174px;
    border: 4px solid var(--brand-green);
    background: radial-gradient(ellipse at 50% 55%, var(--portrait-light) 0%, #8a4a2c 45%, var(--portrait-dark) 100%);
  }
  .name-plate {
    position: absolute;
    left: 369px;
    top: 265px;
    width: 320px;
    height: 52px;
    border: 4px solid var(--brand-green);
    display: flex;
    align-items: center;
    justify-content: center;
    font-size: 38px;
    line-height: 1;
    white-space: nowrap;
  }
  .section-rule {
    position: absolute;
    left: 186px;
    top: 324px;
    width: 698px;
    height: 28px;
    display: flex;
    align-items: center;
  }
  .section-rule::before,
  .section-rule::after {
    content: "";
    flex: 1;
    height: 4px;
    background: var(--brand-green);
  }
  .section-rule span {
    padding: 0 6px;
    font-size: 23px;
    line-height: 1;
  }
  .specialties {
    position: absolute;
    left: 135px;
    top: 370px;
    width: 800px;
    height: 269px;
    border-radius: 58px;
    background: var(--brand-green);
  }
  .specialty-list {
    list-style: none;
    position: absolute;
    color: var(--paper);
    font-size: 25px;
    letter-spacing: 0.3px;
  }
  .specialty-list li {
    position: relative;
    height: 44.5px;
    line-height: 1;
    padding-left: 39px;
  }
  .specialty-list li::before {
    content: "";
    position: absolute;
    left: 0;
    top: -2px;
    width: 28px;
    height: 28px;
    border-radius: 50%;
    background: var(--paper);
  }
  .specialty-list.col-a { left: 115px; top: 70px; }
  .specialty-list.col-b { left: 418px; top: 70px; }
  .specialty-list.col-b li { padding-left: 36px; }
</style>
</head>
<body>
  <main class="card">
    <div class="portrait" role="img" aria-label="Head-and-shoulders portrait photo of Dr Moira Crandle"></div>
    <div class="name-plate">Dr. Moira Crandle</div>
    <div class="section-rule"><span>Specialises in:</span></div>
    <section class="specialties">
      <ul class="specialty-list col-a">
        <li>Nutrigenomics</li>
        <li>Healthy Ageing</li>
        <li>Autism / ADHD</li>
      </ul>
      <ul class="specialty-list col-b">
        <li>Gut Issues</li>
        <li>Food Intolerances</li>
      </ul>
    </section>
    <div class="side-band"></div>
  </main>
</body>
</html>
```